Medical software helping patients with dry eye disease needs a business card

We have a logo we just need a design for a business card for a Canadian company called LUMA: Dry Eye. We use AI technology to assist optometrists in properly diagnosing patients with dry eye disease reducing wait times in doctors offices and accuracy of diagnosis as well as identifying key possible indicators and tailored treatment plans. The final design should be clean and medical looking. Our mission is to help patients and our logo using blues and whites.

```html
<!DOCTYPE html>
<html lang="en">
<head>
<meta charset="utf-8">
<title>LUMA: Dry Eye – Business Card</title>
<link rel="stylesheet" href="https://fonts.googleapis.com/css2?family=Lato:wght@400;700;900&display=swap">
<style>
  :root {
    --navy: #10467a;
    --sky: #29abe2;
    --white: #ffffff;
    --ink: #3a3a3a;
    --backdrop: #3b3b3b;
  }
  * { margin: 0; padding: 0; box-sizing: border-box; }
  html, body { width: 1200px; height: 689px; overflow: hidden; }
  body {
    background: var(--backdrop);
    font-family: "Lato", sans-serif;
    position: relative;
  }
  .card {
    position: absolute;
    top: 196px;
    width: 520px;
    height: 297px;
    border-radius: 16px;
    overflow: hidden;
    box-shadow: 0 14px 30px rgba(0,0,0,0.45);
  }
  .card-back { left: 50px; background: var(--navy); }
  .card-front { left: 630px; background: var(--white); }

  /* back side */
  .back-brand {
    position: absolute; left: 0; right: 0; top: 96px;
    display: flex; align-items: center; justify-content: center; gap: 14px;
  }
  .brand-dot {
    width: 34px; height: 34px; border-radius: 50%; background: var(--white);
  }
  .brand-name {
    color: var(--white); font-weight: 900; font-size: 34px; letter-spacing: 1px;
  }
  .back-url {
    position: absolute; left: 0; right: 0; top: 206px; text-align: center;
    color: var(--white); font-size: 13px; letter-spacing: 6px; font-weight: 400;
  }

  /* front side */
  .front-shape { position: absolute; inset: 0; }
  .front-brand {
    position: absolute; left: 70px; top: 58px;
    display: flex; align-items: center; gap: 10px;
  }
  .front-brand .brand-dot { width: 24px; height: 24px; }
  .front-brand .brand-name { font-size: 26px; }
  .holder {
    position: absolute; left: 34px; top: 232px;
  }
  .holder-name {
    color: var(--navy); font-weight: 900; font-size: 24px; letter-spacing: 0.5px;
  }
  .holder-role {
    color: var(--sky); font-size: 14px; font-weight: 400; margin-top: 2px;
  }
  .divider {
    position: absolute; left: 318px; top: 168px; width: 1.5px; height: 92px;
    background: var(--navy);
  }
  .contacts {
    position: absolute; left: 332px; top: 166px; list-style: none;
    color: var(--ink); font-size: 11.5px; line-height: 1.35;
  }
  .contacts li { display: flex; align-items: flex-start; gap: 8px; margin-bottom: 7px; }
  .contacts svg { flex: none; margin-top: 2px; }
  .contacts .phone { font-weight: 700; font-size: 14px; }
</style>
</head>
<body>

<section class="card card-back">
  <div class="back-brand">
    <span class="brand-dot"></span>
    <span class="brand-name">LUMA DRY EYE</span>
  </div>
  <p class="back-url">WWW.LUMADRYEYE.COM</p>
</section>

<section class="card card-front">
  <svg class="front-shape" viewBox="0 0 520 297" width="520" height="297">
    <path d="M0 0 H520 V58 C440 66 370 112 300 168 C230 218 110 226 0 226 Z" fill="var(--navy)"/>
    <path d="M100 238 C190 228 250 200 310 160 C360 124 400 96 440 84 C395 108 360 140 315 172 C255 212 190 232 100 238 Z" fill="var(--sky)"/>
  </svg>

  <div class="front-brand">
    <span class="brand-dot"></span>
    <span class="brand-name">LUMA DRY EYE</span>
  </div>

  <div class="holder">
    <p class="holder-name">DANIEL WHITFORD</p>
    <p class="holder-role">Founder &amp; CEO</p>
  </div>

  <div class="divider"></div>

  <ul class="contacts">
    <li>
      <svg width="11" height="14" viewBox="0 0 11 14"><path d="M5.5 0 C2.5 0 0 2.3 0 5.3 C0 9 5.5 14 5.5 14 S11 9 11 5.3 C11 2.3 8.5 0 5.5 0 Z" fill="var(--sky)"/><circle cx="5.5" cy="5.3" r="2" fill="var(--white)"/></svg>
      <span>220 1450 Birchwood Rd SW<br>Calgary, AB T3K 8P5</span>
    </li>
    <li>
      <svg width="12" height="12" viewBox="0 0 12 12"><path d="M2.5 0.5 L4.5 3 L3.3 4.4 C4 6 6 8 7.6 8.7 L9 7.5 L11.5 9.5 L10 11.5 C5 11 1 7 0.5 2 Z" fill="var(--sky)"/></svg>
      <span class="phone">587-555-0142</span>
    </li>
    <li>
      <svg width="13" height="10" viewBox="0 0 13 10"><rect x="0.5" y="0.5" width="12" height="9" fill="none" stroke="var(--sky)"/><path d="M0.5 0.5 L6.5 5.5 L12.5 0.5" fill="none" stroke="var(--sky)"/></svg>
      <span>hello@lumadryeye.com</span>
    </li>
  </ul>
</section>

</body>
</html>
```